Business Card Design Project

Black Writing

Jade Owlet

Target Market(s)

18 - 80 year olds

Industry/Entity Type

Business

Requirements
Must have
• Clean

```html
<!DOCTYPE html>
<html lang="en">
<head>
<meta charset="utf-8">
<title>Jade Owlet – Business Card</title>
<link rel="stylesheet" href="https://fonts.googleapis.com/css2?family=Arimo:wght@400;700&family=Playfair+Display:wght@700&display=swap">
<style>
  :root {
    --page-bg: #ffffff;
    --card-edge: #000000;
    --gold-light: #e9d28e;
    --gold-mid: #b8933f;
    --gold-dark: #7a5d22;
    --name-gold: #a8883c;
    --panel-top: #ffffff;
    --panel-bottom: #dcdcdc;
    --ink: #111111;
    --badge-fill: #e6e6e6;
    --badge-line: #9a9a9a;
  }
  * { margin: 0; padding: 0; box-sizing: border-box; }
  html, body {
    width: 1200px;
    height: 900px;
    overflow: hidden;
    background: var(--page-bg);
  }
  .card {
    position: absolute;
    left: 98px;
    top: 113px;
    width: 1022px;
    height: 610px;
    background: var(--card-edge);
  }
  .card__frame {
    position: absolute;
    inset: 21px;
    padding: 8px;
    background: linear-gradient(135deg, var(--gold-dark), var(--gold-light) 30%, var(--gold-mid) 55%, var(--gold-light) 80%, var(--gold-dark));
  }
  .card__panel {
    position: relative;
    width: 100%;
    height: 100%;
    background: linear-gradient(180deg, var(--panel-top) 0%, #f4f4f4 45%, var(--panel-bottom) 100%);
  }
  .holder {
    position: absolute;
    right: 35px;
    top: 32px;
    text-align: right;
    font-family: "Arimo", Arial, sans-serif;
  }
  .holder__name {
    color: var(--name-gold);
    font-size: 30px;
    line-height: 1.1;
  }
  .holder__role {
    color: var(--ink);
    font-size: 24px;
    margin-top: 4px;
  }
  .brand__mark {
    position: absolute;
    left: 398px;
    top: 93px;
    width: 206px;
    height: 206px;
    border-radius: 50%;
    background: var(--ink);
  }
  .brand__name {
    position: absolute;
    left: 301px;
    width: 400px;
    top: 301px;
    text-align: center;
    font-family: "Playfair Display", Georgia, serif;
    font-weight: 700;
    font-size: 50px;
    color: var(--ink);
    line-height: 60px;
  }
  .contacts {
    position: absolute;
    left: 23px;
    top: 391px;
    list-style: none;
    font-family: "Arimo", Arial, sans-serif;
    font-size: 30px;
    color: var(--ink);
  }
  .contacts__item {
    display: flex;
    align-items: center;
    height: 39px;
  }
  .contacts__icon {
    width: 36px;
    height: 36px;
    margin-right: 10px;
    fill: var(--gold-mid);
  }
  .partner-badge {
    position: absolute;
    left: 721px;
    top: 389px;
    width: 226px;
    height: 153px;
    background: var(--badge-fill);
    border: 2px solid var(--badge-line);
  }
</style>
</head>
<body>
  <div class="card">
    <div class="card__frame">
      <div class="card__panel">
        <div class="holder">
          <p class="holder__name">Milo Trent</p>
          <p class="holder__role">Manager</p>
        </div>

        <div class="brand__mark"></div>
        <p class="brand__name">Jade Owlet</p>

        <ul class="contacts">
          <li class="contacts__item">
            <svg class="contacts__icon" viewBox="0 0 24 24" aria-hidden="true"><path d="M6.6 10.8a15.1 15.1 0 0 0 6.6 6.6l2.2-2.2a1 1 0 0 1 1-.25 11.4 11.4 0 0 0 3.6.57 1 1 0 0 1 1 1V20a1 1 0 0 1-1 1A17 17 0 0 1 3 4a1 1 0 0 1 1-1h3.5a1 1 0 0 1 1 1c0 1.250.2 2.450.57 3.6a1 1 0 0 1-.25 1z"/></svg>
            <span>1535 204 718</span>
          </li>
          <li class="contacts__item">
            <svg class="contacts__icon" viewBox="0 0 24 24" aria-hidden="true"><path d="M12 2a10 10 0 1 0 0 20 10 10 0 0 0 0-20zm6.9 6h-2.9a15.6 15.6 0 0 0-1.4-3.6A8 8 0 0 1 18.9 8zM12 4c.8 1.2 1.5 2.5 1.9 4h-3.8c.4-1.4 1.1-2.8 1.9-4zM4.3 14a8 8 0 0 1 0-4h3.4a16 16 0 0 0 0 4zm.8 2h2.9c.3 1.3.8 2.5 1.4 3.6A8 8 0 0 1 5.1 16zM8 8H5.1a8 8 0 0 1 4.3-3.6C8.8 5.5 8.3 6.7 8 8zm4 12c-.8-1.2-1.5-2.5-1.9-4h3.8c-.4 1.4-1.1 2.8-1.9 4zm2.3-6H9.7a14.6 14.6 0 0 1 0-4h4.6a14.6 14.6 0 0 1 0 4zm.3 5.6c.6-1.1 1.1-2.3 1.4-3.6h2.9a8 8 0 0 1-4.3 3.6zm1.7-5.6a16 16 0 0 0 0-4h3.4a8 8 0 0 1 0 4z"/></svg>
            <span>www.jadeowlet.com</span>
          </li>
          <li class="contacts__item">
            <svg class="contacts__icon" viewBox="0 0 24 24" aria-hidden="true"><path d="M2 6a2 2 0 0 1 2-2h16a2 2 0 0 1 2 2v12a2 2 0 0 1-2 2H4a2 2 0 0 1-2-2zm2 .5V8l8 5 8-5V6.5l-8 5z"/></svg>
            <span>info@jadeowlet.com</span>
          </li>
          <li class="contacts__item">
            <svg class="contacts__icon" viewBox="0 0 24 24" aria-hidden="true"><path d="M12 3 1 12h3v9h6v-6h4v6h6v-9h3z"/></svg>
            <span>PO Box 7120 Harbour Plaza Nlt 6093</span>
          </li>
        </ul>

        <div class="partner-badge" role="img" aria-label="Partner badge"></div>
      </div>
    </div>
  </div>
</body>
</html>
```